Gutschein für Onlineshop DIN A Lang
Zielgruppe
Wir betreiben unter www.feldkiste-online.example einen Onlineshop für Armee- und Outdoorbekleidung sowie Ausrüstung. Für eine Paketbeilage benötigen wir einen Gutschein
Aufgabenstellung
Erstellung eines Gutscheins im DIN A Lang Format (Kuvert) mit Vorder- und Rückseite im CI der Webseite. Logo kann gerne zur Verfügung gestellt werden.
Gutscheincode, Wert und Laufzeit wird noch mitgeteilt.

```html
<!DOCTYPE html>
<html lang="de">
<head>
<meta charset="utf-8">
<title>Feldkiste – 25 € Gutschein DIN lang</title>
<link rel="stylesheet" href="https://fonts.googleapis.com/css2?family=Arimo:wght@400;700&family=Oswald:wght@700&family=Stardos+Stencil:wght@700&display=swap">
<style>
  :root {
    --olive: #4a4f37;
    --olive-dark: #3c402c;
    --leaf: #8ea05e;
    --code-bg: #c8d59c;
    --paper: #ffffff;
    --ink: #3a3d2c;
    --ground: #e6e4df;
    --badge: #d9d9d9;
  }
  * { box-sizing: border-box; margin: 0; padding: 0; }
  html, body { width: 1200px; height: 1200px; overflow: hidden; }
  body { background: var(--ground); font-family: "Arimo", Arial, sans-serif; color: var(--ink); position: relative; }

  .voucher { position: absolute; left: 50px; width: 1100px; height: 500px; background: var(--paper); box-shadow: 0 4px 14px rgba(0,0,0,.18); }
  .voucher--front { top: 60px; }
  .voucher--back { top: 640px; }

  /* Front */
  .front__camo { position: absolute; left: 12px; top: 12px; width: 88px; height: 476px;
    background: linear-gradient(180deg, #6b6a45 0%, #b69d6c 35%, #5a5a3a 60%, #c3ab7c 100%); }
  .front__brands { position: absolute; left: 100px; top: 12px; width: 210px; height: 476px; padding: 20px 16px; }
  .brand-name { display: flex; align-items: center; gap: 10px; font-weight: 700; font-size: 30px; color: var(--olive); letter-spacing: .5px; margin: 10px 0 60px; }
  .brand-name__mark { width: 18px; height: 18px; background: var(--leaf); }
  .partner-grid { display: grid; grid-template-columns: 1fr 1fr; gap: 8px; }
  .partner-badge { height: 48px; border: 1px solid #bbb; background: var(--badge); }
  .front__photo { position: absolute; left: 310px; top: 12px; width: 778px; height: 476px;
    background: linear-gradient(135deg, #4b4a3a 0%, #8b7d5a 40%, #b9a374 60%, #4d5a34 100%); }
  .front__tag { position: absolute; left: 395px; top: 190px; width: 520px; height: 170px; transform: rotate(-7deg);
    background: linear-gradient(180deg, #c9cbcd, #9c9fa2); border: 2px solid #8a8d90; border-radius: 10px;
    display: flex; align-items: center; justify-content: center; box-shadow: 0 8px 18px rgba(0,0,0,.35);
    font-family: "Oswald", "Arial Narrow", sans-serif; font-weight: 700; font-size: 80px; color: #151515; letter-spacing: -1px; }
  .front__tag::after { content: ""; position: absolute; right: 22px; top: 18px; width: 20px; height: 20px; border-radius: 50%; background: #555; }
  .front__url { position: absolute; right: 12px; bottom: 50px; background: var(--olive); color: #fff; font-weight: 700; font-size: 20px; padding: 10px 30px 10px 40px; }

  /* Back */
  .back__panel { position: absolute; left: 12px; top: 12px; width: 455px; height: 476px; background: var(--olive); color: #fff; padding: 28px 40px; overflow: hidden; }
  .back__value { font-family: "Stardos Stencil", Impact, sans-serif; font-weight: 700; font-size: 150px; line-height: .95; }
  .back__title { font-family: "Stardos Stencil", Impact, sans-serif; font-weight: 700; font-size: 60px; line-height: 1; margin-top: 4px; }
  .back__code-label { font-size: 16px; margin-top: 24px; }
  .back__code { margin-top: 6px; background: var(--code-bg); color: var(--olive-dark); font-size: 34px; font-weight: 700; text-align: center; padding: 4px 0; letter-spacing: 1px; }
  .back__terms { font-size: 15px; line-height: 1.3; margin-top: 18px; }
  .back__terms strong { font-weight: 700; }
  .back__content { position: absolute; left: 500px; top: 40px; right: 40px; bottom: 30px; }
  .back__content .brand-name { position: absolute; right: 0; top: 0; margin: 0; }
  .back__headline { position: absolute; top: 150px; font-weight: 700; font-size: 18px; }
  .benefits { position: absolute; top: 195px; list-style: none; font-size: 15.5px; line-height: 1.35; }
  .benefits li { display: flex; gap: 10px; margin-bottom: 12px; }
  .benefits svg { flex: none; margin-top: 3px; }
  .back__footer { position: absolute; bottom: 20px; font-size: 16px; }
  .back__footer strong { font-weight: 700; }
</style>
</head>
<body>

<section class="voucher voucher--front">
  <div class="front__camo" role="img" aria-label="Tarnmuster-Stoff"></div>
  <div class="front__brands">
    <div class="brand-name"><span class="brand-name__mark"></span>Feldkiste</div>
    <div class="partner-grid">
      <div class="partner-badge"></div><div class="partner-badge"></div>
      <div class="partner-badge"></div><div class="partner-badge"></div>
      <div class="partner-badge"></div><div class="partner-badge"></div>
      <div class="partner-badge"></div><div class="partner-badge"></div>
      <div class="partner-badge"></div><div class="partner-badge"></div>
      <div class="partner-badge"></div><div class="partner-badge"></div>
    </div>
  </div>
  <div class="front__photo" role="img" aria-label="Foto: Messer in Scheide auf Tarnstoff und Flecktarn-Ausrüstung"></div>
  <div class="front__tag">25€ GUTSCHEIN</div>
  <div class="front__url">www.feldkiste-online.example</div>
</section>

<section class="voucher voucher--back">
  <div class="back__panel">
    <div class="back__value">25 €</div>
    <div class="back__title">GUTSCHEIN</div>
    <p class="back__code-label">Ihr Gutscheincode:</p>
    <div class="back__code">1234567890</div>
    <p class="back__terms">Einmalig einlösbar bis zum XX.XX.2014 unter <strong>www.beispiel-shop.example</strong>. Nicht mit anderen Aktionen kombiniertbar. Nur ein Gutschein pro Kunde.</p>
  </div>
  <div class="back__content">
    <div class="brand-name"><span class="brand-name__mark"></span>Feldkiste</div>
    <h2 class="back__headline">Besuchen Sie uns und entdecken Sie die Welt der Armee</h2>
    <ul class="benefits">
      <li><svg width="14" height="12" viewBox="0 0 14 12"><path d="M1 6l4 4 8-9" fill="none" stroke="#3a3d2c" stroke-width="2.5"/></svg><span>fast 10 Jahre Bundeswehr-Shop im Internet</span></li>
      <li><svg width="14" height="12" viewBox="0 0 14 12"><path d="M1 6l4 4 8-9" fill="none" stroke="#3a3d2c" stroke-width="2.5"/></svg><span>größen Auswahl an Bundeswehrbekleidung,<br>Armeebekleidung sowie umfangreiche Ausrüstung<br>für Arbeit, Hobby und Freizeit</span></li>
      <li><svg width="14" height="12" viewBox="0 0 14 12"><path d="M1 6l4 4 8-9" fill="none" stroke="#3a3d2c" stroke-width="2.5"/></svg><span>sofort Lieferung in 24Stunden</span></li>
      <li><svg width="14" height="12" viewBox="0 0 14 12"><path d="M1 6l4 4 8-9" fill="none" stroke="#3a3d2c" stroke-width="2.5"/></svg><span>gratis versand ab 100€ Bestellwert</span></li>
    </ul>
    <p class="back__footer"><strong>www.feldkiste-online.example</strong> | kostenlose Hotline <strong>0 12 34-5 67 89 00</strong></p>
  </div>
</section>

</body>
</html>
```